IT Consulting Company needs a PowerPoint Template Design

We need a PowerPoint template design for an IT Consulting company called "Corvenza" (www.corvenza-example.com). We provide IT consulting services to customers. We mostly use the PowerPoint to present diagram, tables, lots of text. So, we would like to see the designs that is bold, modern and easy to read text. There should be the attached logo on every slides. The final design should communicate "Most Trusted IT Advisor".

Industry/Entity Type

It Company

Requirements
Must have
• The PowerPoint Template must have the following pages:
1. Title Slide (Main Title, Sub Title, Speaker, Date)
2. Title and Content (Bulleted content)
3. Title and Content (Numbered content)
4. Title and Table (Multiple columns with header and footer)
5. General Section header (Main Title, Sub Title)
6. Section header ("Demo" with graphic)
7. Section header ("Q&A" with graphic)
8. Section header ("Business Requirement" with graphic)
9. Section header ("Progress Update" with graphic)
10. Section header ("Project Plan" with graphic)
11. Closing Slide ("Thank you" with graphic)
Nice to have
• We prefer color blue. But other colors are welcome.

```html
<!DOCTYPE html>
<html lang="en">
<head>
<meta charset="utf-8">
<title>Corvenza – Presentation Template Overview</title>
<link href="https://fonts.googleapis.com/css2?family=Source+Sans+3:wght@300;400;600;700&display=swap" rel="stylesheet">
<style>
  :root {
    --navy: #2d4e77;
    --navy-deep: #24405f;
    --ink: #1e2834;
    --accent: #e63b2e;
    --text: #3a4350;
    --link-blue: #2a5ea8;
    --canvas: #a8acb1;
    --white: #ffffff;
    --row-a: #f2f3f5;
    --row-b: #ffffff;
  }
  * { box-sizing: border-box; margin: 0; padding: 0; }
  html, body { width: 1060px; height: 1200px; overflow: hidden; background: var(--canvas); }
  body { font-family: "Source Sans 3", "Helvetica Neue", Arial, sans-serif; color: var(--text); }

  .sheet { position: relative; width: 1060px; height: 1200px; }

  .slide { position: absolute; width: 514px; height: 385px; overflow: hidden; background: var(--white); }
  .col-left  { left: 12px; }
  .col-right { left: 534px; }
  .row-1 { top: 9px; }
  .row-2 { top: 405px; }
  .row-3 { top: 802px; }

  /* Wordmark */
  .wordmark { font-weight: 400; letter-spacing: 0.02em; line-height: 1; white-space: nowrap; }

  /* Cover */
  .cover-plain { background: linear-gradient(135deg, #ffffff 0%, #f1f3f6 100%); }
  .cover-plain .wordmark { position: absolute; left: 83px; top: 160px; font-size: 72px; color: var(--navy); }

  .cover-photo .photo {
    position: absolute; inset: 0;
    background: linear-gradient(120deg, #dfe9f5 0%, #9fbbe0 35%, #5f86bd 65%, #2f4e7c 100%);
  }
  .cover-photo .title-box { position: absolute; left: 0; top: 165px; width: 262px; height: 132px; background: var(--navy); }
  .cover-photo .title-box .wordmark { position: absolute; left: 31px; top: 44px; font-size: 44px; color: var(--white); }
  .cover-photo .presenter-band { position: absolute; left: 0; top: 297px; width: 262px; height: 54px; background: rgba(22, 30, 42, 0.85); }
  .presenter-band .name { position: absolute; right: 10px; top: 9px; font-size: 12px; color: var(--white); }
  .presenter-band .audience { position: absolute; right: 10px; top: 27px; font-size: 8px; color: var(--white); }
  .cover-photo .event { position: absolute; left: 271px; top: 300px; font-size: 36px; font-weight: 300; color: var(--white); line-height: 1; }
  .cover-photo .event-date { position: absolute; left: 318px; top: 355px; font-size: 12px; color: var(--white); }

  /* Content slide chrome */
  .slide-header { position: absolute; left: 0; top: 0; width: 514px; height: 52px; background: var(--navy); color: var(--white); }
  .slide-header .project { position: absolute; left: 8px; top: 9px; font-size: 18px; font-weight: 600; letter-spacing: -0.01em; line-height: 1; }
  .slide-header .subtitle { position: absolute; left: 8px; top: 29px; font-size: 13px; line-height: 1; }
  .slide-header .event { position: absolute; right: 32px; top: 4px; font-size: 17px; font-weight: 300; line-height: 1; }
  .slide-header .event-date { position: absolute; right: 44px; top: 23px; font-size: 5px; }

  .slide-footer { position: absolute; left: 0; bottom: 0; width: 514px; height: 26px; background: var(--ink); color: var(--white); display: flex; align-items: center; }
  .slide-footer .page-no { width: 31px; height: 26px; background: var(--navy); font-size: 8px; font-weight: 700; display: flex; align-items: center; justify-content: center; }
  .slide-footer .wordmark { margin-left: 16px; font-size: 14px; }
  .slide-footer .audience { margin-left: 6px; font-size: 7px; }
  .slide-footer .audience b { font-weight: 700; }

  .content-title { position: absolute; font-size: 15px; color: var(--navy-deep); line-height: 1; }
  .content-title b { font-weight: 700; }

  .bullets { position: absolute; list-style: none; font-size: 8.6px; line-height: 1.5; }
  .bullets li { position: relative; padding-left: 14px; margin-bottom: 11px; }
  .bullets li::before {
    content: ""; position: absolute; left: 0; top: 4px;
    border-left: 4px solid var(--accent); border-top: 3px solid transparent; border-bottom: 3px solid transparent;
  }
  .bullets li.level-2 { margin-left: 30px; }
  .bullets li.level-3 { margin-left: 48px; font-weight: 700; color: var(--navy-deep); margin-bottom: 6px; }
  .bullets li.emphasis { font-weight: 700; color: var(--link-blue); }
  .bullets b { color: var(--navy-deep); }

  .table-text { left: 34px; top: 112px; width: 154px; text-align: justify; }

  /* Table */
  .data-table { position: absolute; left: 214px; top: 94px; width: 277px; border-collapse: collapse; box-shadow: 0 2px 4px rgba(0,0,0,0.25); font-size: 8px; text-align: center; }
  .data-table th { height: 31px; background: var(--navy); color: var(--white); font-size: 12px; font-weight: 700; border-right: 1px solid #6f89ad; }
  .data-table th:last-child { border-right: 0; }
  .data-table th.highlight { color: var(--accent); }
  .data-table td { height: 35px; color: var(--text); border-right: 1px solid #e3e6ea; }
  .data-table td:last-child { border-right: 0; }
  .data-table tbody tr:nth-child(odd) td { background: var(--row-a); }
  .data-table tbody tr:nth-child(even) td { background: var(--row-b); }
  .data-table tfoot td { height: 21px; background: var(--ink); color: var(--white); font-weight: 600; }

  /* Charts */
  .chart { position: absolute; left: 0; top: 0; }
  .chart text { font-family: "Source Sans 3", Arial, sans-serif; }
  .chart-note { position: absolute; list-style: none; font-size: 6.5px; line-height: 1.45; width: 200px; }
  .chart-note li { position: relative; padding-left: 13px; margin-bottom: 9px; }
  .chart-note li::before {
    content: ""; position: absolute; left: 0; top: 2px;
    border-left: 3px solid var(--accent); border-top: 2.5px solid transparent; border-bottom: 2.5px solid transparent;
  }
  .chart-note b { color: var(--navy-deep); }

  /* Closing */
  .closing { background: radial-gradient(circle at 50% 45%, #33567f 0%, #2b4b72 60%, #263f61 100%); }
  .closing .wordmark { position: absolute; left: 0; width: 514px; text-align: center; top: 158px; font-size: 74px; color: var(--white); }
  .closing .web { position: absolute; left: 0; width: 514px; text-align: center; top: 238px; font-size: 14px; letter-spacing: 0.2em; color: var(--white); font-weight: 600; }
</style>
</head>
<body>
<main class="sheet">

  <!-- Cover, plain -->
  <section class="slide cover-plain col-left row-1">
    <div class="wordmark">Corvenza</div>
  </section>

  <!-- Cover with photo -->
  <section class="slide cover-photo col-right row-1">
    <div class="photo" role="img" aria-label="Photo of a person in a light blue shirt tapping a tablet screen"></div>
    <div class="title-box"><div class="wordmark">Corvenza</div></div>
    <div class="presenter-band">
      <div class="name">Name of the Presenter</div>
      <div class="audience">to <b>Client</b>/Customer</div>
    </div>
    <div class="event">Explore.</div>
    <div class="event-date">June 2013</div>
  </section>

  <!-- Bulleted content -->
  <section class="slide col-left row-2">
    <header class="slide-header">
      <div class="project">PROJECT TITLE</div>
      <div class="subtitle">Project Subtitle</div>
      <div class="event">Explore.</div>
      <div class="event-date">June 2013</div>
    </header>
    <h2 class="content-title" style="left:36px; top:93px;"><b>Content</b> Title</h2>
    <ul class="bullets" style="left:24px; top:125px; width:470px;">
      <li><b>Aenean</b> ridiculus tortor quis interdum id habitant ad, natoque consectetuer nisl auctor libero quisque euismod ante inceptos malesuada ligula mattis.</li>
      <li class="level-2">Nulla, netus pulvinar pellentesque porttitor purus maecenas tellus hac nulla lacus. Lorem. Nostra laoreet nulla, dis cursus nascetur dolor odio Eu Magna molestie montes dui mus cursus habitasse mauris tempor.</li>
      <li class="level-2 emphasis">Varius inceptos nascetur mollis dui aptent ultrices. Pretium pulvinar ante lobortis convallis lectus netus vitae penatibus eros at blandit. Parturient.</li>
      <li class="level-3">Aenean</li>
      <li class="level-3">Nascetur</li>
      <li class="level-3" style="margin-bottom:11px;">Pellentesque</li>
      <li><b>Aenean</b> ridiculus tortor quis interdum id habitant ad, natoque consectetuer nisl auctor libero quisque euismod ante inceptos malesuada ligula mattis.</li>
    </ul>
    <footer class="slide-footer">
      <div class="page-no">3</div>
      <div class="wordmark">Corvenza</div>
      <div class="audience">| To <b>Client</b>/Customer</div>
    </footer>
  </section>

  <!-- Table -->
  <section class="slide col-right row-2">
    <header class="slide-header">
      <div class="project">PROJECT TITLE</div>
      <div class="subtitle">Project Subtitle</div>
      <div class="event">Explore.</div>
      <div class="event-date">June 2013</div>
    </header>
    <h2 class="content-title" style="left:33px; top:90px;"><b>Table</b> Explanation</h2>
    <ul class="bullets table-text">
      <li><b>Aenean</b> ridiculus tortor quis interdum id habitant ad, natoque consectetuer nisl auctor libero quisque euismod ante inceptos malesuada ligula mattis.</li>
      <li>Nulla, netus pulvinar pellentesque porttitor purus maecenas tellus hac nulla lacus. Lorem. Nostra laoreet nulla, dis cursus nascetur dolor odio Eu Magna molestie montes dui mus cursus habitasse mauris tempor.</li>
      <li>Varius inceptos <b>nascetur</b> mollis dui aptent ultrices. Pretium pulvinar ante lobortis convallis lectus netus vitae penatibus eros at blandit. Parturient.</li>
    </ul>
    <table class="data-table">
      <thead>
        <tr><th>Q1</th><th>Q2</th><th class="highlight">Q3</th><th>Q4</th></tr>
      </thead>
      <tbody>
        <tr><td>Amount</td><td>Information</td><td>Amount</td><td>Information</td></tr>
        <tr><td>Amount</td><td>Information</td><td>Amount</td><td>Information</td></tr>
        <tr><td>Amount</td><td>Information</td><td>Amount</td><td>Information</td></tr>
        <tr><td>Amount</td><td>Information</td><td>Amount</td><td>Information</td></tr>
        <tr><td>Amount</td><td>Information</td><td>Amount</td><td>Information</td></tr>
      </tbody>
      <tfoot>
        <tr><td></td><td></td><td></td><td>Other</td></tr>
      </tfoot>
    </table>
    <footer class="slide-footer">
      <div class="page-no">4</div>
      <div class="wordmark">Corvenza</div>
      <div class="audience">| To <b>Client</b>/Customer</div>
    </footer>
  </section>

  <!-- Charts -->
  <section class="slide col-left row-3">
    <header class="slide-header">
      <div class="project">PROJECT TITLE</div>
      <div class="subtitle">Project Subtitle</div>
      <div class="event">Explore.</div>
      <div class="event-date">June 2013</div>
    </header>
    <h2 class="content-title" style="left:36px; top:89px;"><b>Graph</b> Title</h2>
    <h2 class="content-title" style="left:296px; top:89px;"><b>Graph</b> Title</h2>

    <svg class="chart" width="514" height="385" viewBox="0 0 514 385" aria-label="Column and bar charts by year">
      <defs>
        <linearGradient id="col-dark" x1="0" x2="1"><stop offset="0" stop-color="#1c2d45"/><stop offset="1" stop-color="#2e4567"/></linearGradient>
        <linearGradient id="col-mid" x1="0" x2="1"><stop offset="0" stop-color="#244f82"/><stop offset="1" stop-color="#3a6ca6"/></linearGradient>
        <linearGradient id="col-light" x1="0" x2="1"><stop offset="0" stop-color="#3f8fd4"/><stop offset="1" stop-color="#6db6ee"/></linearGradient>
        <linearGradient id="bar-blue" x1="0" y1="0" x2="0" y2="1"><stop offset="0" stop-color="#3472b5"/><stop offset="1" stop-color="#1f4f88"/></linearGradient>
        <linearGradient id="bar-red" x1="0" y1="0" x2="0" y2="1"><stop offset="0" stop-color="#d6466a"/><stop offset="1" stop-color="#9c2443"/></linearGradient>
        <linearGradient id="bar-grey" x1="0" y1="0" x2="0" y2="1"><stop offset="0" stop-color="#eef0f6"/><stop offset="1" stop-color="#c5cbdc"/></linearGradient>
      </defs>

      <!-- Column chart -->
      <g font-size="6.5" fill="#2d3b4e" font-weight="700">
        <g stroke="#c9ced6" stroke-width="0.6">
          <line x1="40" y1="106" x2="224" y2="106"/>
          <line x1="40" y1="140.5" x2="224" y2="140.5"/>
          <line x1="40" y1="175" x2="224" y2="175"/>
          <line x1="40" y1="209.5" x2="224" y2="209.5"/>
        </g>
        <line x1="40" y1="244" x2="224" y2="244" stroke="#8a93a0" stroke-width="0.8"/>
        <text x="30" y="108" text-anchor="end">100</text>
        <text x="30" y="142.5" text-anchor="end">75</text>
        <text x="30" y="177" text-anchor="end">50</text>
        <text x="30" y="211.5" text-anchor="end">25</text>
        <text x="30" y="246" text-anchor="end">0</text>

        <rect x="43" y="220.5" width="12" height="23.5" fill="url(#col-dark)"/>
        <rect x="56" y="202.6" width="12" height="41.4" fill="url(#col-mid)"/>
        <rect x="69" y="168.1" width="12" height="75.9" fill="url(#col-light)"/>

        <rect x="90" y="208.1" width="12" height="35.9" fill="url(#col-dark)"/>
        <rect x="103" y="221.9" width="12" height="22.1" fill="url(#col-mid)"/>
        <rect x="116" y="184.7" width="12" height="59.3" fill="url(#col-light)"/>

        <rect x="137" y="170.9" width="12" height="73.1" fill="url(#col-dark)"/>
        <rect x="150" y="206.7" width="12" height="37.3" fill="url(#col-mid)"/>
        <rect x="163" y="147.4" width="12" height="96.6" fill="url(#col-light)"/>

        <rect x="184" y="111.5" width="12" height="132.5" fill="url(#col-dark)"/>
        <rect x="197" y="181.9" width="12" height="62.1" fill="url(#col-mid)"/>
        <rect x="210" y="164" width="12" height="80" fill="url(#col-light)"/>

        <text x="62" y="254" text-anchor="middle">2007</text>
        <text x="109" y="254" text-anchor="middle">2008</text>
        <text x="156" y="254" text-anchor="middle">2009</text>
        <text x="203" y="254" text-anchor="middle">2010</text>
      </g>

      <!-- Horizontal bar chart -->
      <g font-size="6.5" fill="#2d3b4e" font-weight="700">
        <g stroke="#c9ced6" stroke-width="0.6">
          <line x1="339.75" y1="104" x2="339.75" y2="245"/>
          <line x1="383.5" y1="104" x2="383.5" y2="245"/>
          <line x1="427.25" y1="104" x2="427.25" y2="245"/>
          <line x1="471" y1="104" x2="471" y2="245"/>
        </g>
        <line x1="296" y1="104" x2="296" y2="245" stroke="#8a93a0" stroke-width="0.8"/>

        <rect x="296" y="106" width="29.8" height="9" fill="url(#bar-blue)"/>
        <rect x="296" y="116.5" width="52.5" height="9" fill="url(#bar-red)"/>
        <rect x="296" y="127" width="96.3" height="9" fill="url(#bar-grey)"/>

        <rect x="296" y="142" width="45.5" height="9" fill="url(#bar-blue)"/>
        <rect x="296" y="152.5" width="28" height="9" fill="url(#bar-red)"/>
        <rect x="296" y="163" width="77" height="9" fill="url(#bar-grey)"/>

        <rect x="296" y="178" width="92.8" height="9" fill="url(#bar-blue)"/>
        <rect x="296" y="188.5" width="47.3" height="9" fill="url(#bar-red)"/>
        <rect x="296" y="199" width="122.5" height="9" fill="url(#bar-grey)"/>

        <rect x="296" y="214" width="168" height="9" fill="url(#bar-blue)"/>
        <rect x="296" y="224.5" width="78.8" height="9" fill="url(#bar-red)"/>
        <rect x="296" y="235" width="101.5" height="9" fill="url(#bar-grey)"/>

        <text x="289" y="122" text-anchor="end">2007</text>
        <text x="289" y="158" text-anchor="end">2008</text>
        <text x="289" y="194" text-anchor="end">2009</text>
        <text x="289" y="230" text-anchor="end">2010</text>

        <text x="296" y="255" text-anchor="middle">0</text>
        <text x="339.75" y="255" text-anchor="middle">25</text>
        <text x="383.5" y="255" text-anchor="middle">50</text>
        <text x="427.25" y="255" text-anchor="middle">75</text>
        <text x="471" y="255" text-anchor="middle">100</text>
      </g>
    </svg>

    <ul class="chart-note" style="left:32px; top:262px;">
      <li><b>Aenean</b> ridiculus tortor quis interdum id habitant ad, natoque consectetuer nisl auctor libero quisque euismod ante inceptos malesuada ligula mattis.</li>
      <li>Varius inceptos <b>nascetur</b> mollis dui aptent ultrices. Pretium pulvinar ante lobortis convallis lectus netus vitae penatibus eros at blandit. Parturient.</li>
    </ul>
    <ul class="chart-note" style="left:285px; top:262px;">
      <li><b>Aenean</b> ridiculus tortor quis interdum id habitant ad, natoque consectetuer nisl auctor libero quisque euismod ante inceptos malesuada ligula mattis.</li>
      <li>Varius inceptos <b>nascetur</b> mollis dui aptent ultrices. Pretium pulvinar ante lobortis convallis lectus netus vitae penatibus eros at blandit. Parturient.</li>
    </ul>

    <footer class="slide-footer">
      <div class="page-no">5</div>
      <div class="wordmark">Corvenza</div>
      <div class="audience">| To <b>Client</b>/Customer</div>
    </footer>
  </section>

  <!-- Closing -->
  <section class="slide closing col-right row-3">
    <div class="wordmark">Corvenza</div>
    <div class="web">www.corvenza-example.com</div>
  </section>

</main>
</body>
</html>
```